Security doors and flyscreens

We need business cards for our company called K & M Distributors. We quote, manufacture and install security doors and flyscreens.

Industry/Entity Type

Security

Contact Information for Business Card

K & M DISTRIBUTORS
17 Larkvale Rd. Thomastown 3074
Ph: 8157 2604
Fax: 8157 2609
Gavin: 0419 275 916
Email: gatesupplier@mailbox-example.net

```html
<!DOCTYPE html>
<html lang="en">
<head>
<meta charset="utf-8">
<title>K &amp; M Distributors – Business Cards</title>
<link rel="stylesheet" href="https://fonts.googleapis.com/css2?family=Michroma&family=Montserrat:wght@400;500;600&display=swap">
<style>
  :root {
    --bg: #5d5d5f;
    --card-white: #ffffff;
    --card-grey: #eceef0;
    --blue-light: #5cc4f2;
    --blue: #1e9ad8;
    --blue-deep: #1179b8;
    --ink: #2b3a4a;
    --ink-soft: #4e5d6b;
    --icon: #3a3f45;
  }
  * { box-sizing: border-box; margin: 0; padding: 0; }
  html, body { width: 1200px; height: 988px; overflow: hidden; }
  body {
    background: var(--bg);
    display: flex;
    flex-direction: column;
    align-items: center;
    justify-content: center;
    gap: 48px;
    font-family: "Montserrat", sans-serif;
    color: var(--ink);
  }
  .card {
    width: 770px;
    height: 440px;
    position: relative;
    overflow: hidden;
    box-shadow: 0 10px 28px rgba(0,0,0,.35);
  }
  /* back */
  .card-back { background: var(--card-white); }
  .card-back .band {
    position: absolute; left: 0; right: 0; height: 112px;
    background: linear-gradient(90deg, var(--blue-light), var(--blue) 60%, var(--blue-deep));
  }
  .card-back .band-top { top: 0; }
  .card-back .band-bottom { bottom: 0; }
  .brand {
    display: flex; align-items: center; gap: 14px;
    white-space: nowrap;
  }
  .brand-mark {
    width: 34px; height: 34px; background: var(--blue); flex: none;
  }
  .brand-name {
    font-family: "Michroma", sans-serif;
    font-size: 22px; color: var(--ink); letter-spacing: 1px;
  }
  .card-back .brand {
    position: absolute; top: 50%; left: 50%; transform: translate(-50%, -50%);
  }
  /* front */
  .card-front { background: var(--card-grey); }
  .front-panel {
    position: absolute; top: 28px; left: 28px; width: 640px; height: 290px;
    background: var(--card-white);
    padding: 32px 36px;
  }
  .person { margin-top: 26px; }
  .person-name {
    font-family: "Michroma", sans-serif;
    font-size: 19px; color: var(--ink-soft); letter-spacing: 1px;
  }
  .person-title {
    font-size: 13px; letter-spacing: 2px; color: var(--ink-soft); margin-top: 4px;
  }
  .contacts {
    margin-top: 22px;
    display: grid; grid-template-columns: 275px 1fr; row-gap: 12px;
    font-size: 12.5px; color: var(--ink);
  }
  .contact { display: flex; align-items: center; gap: 8px; white-space: nowrap; }
  .contact svg { width: 14px; height: 14px; flex: none; }
  .rule {
    position: absolute; right: 0; height: 7px;
    border-top: 3px solid var(--blue);
    border-bottom: 2px solid var(--blue);
  }
  .rule-upper { top: 334px; left: 300px; }
  .rule-lower { bottom: 28px; left: 250px; }
</style>
</head>
<body>
  <section class="card card-back">
    <div class="band band-top"></div>
    <div class="brand">
      <span class="brand-mark"></span>
      <span class="brand-name">K &amp; M DISTRIBUTORS</span>
    </div>
    <div class="band band-bottom"></div>
  </section>

  <section class="card card-front">
    <div class="front-panel">
      <div class="brand">
        <span class="brand-mark"></span>
        <span class="brand-name">K &amp; M DISTRIBUTORS</span>
      </div>
      <div class="person">
        <p class="person-name">GAVIN MORETTI</p>
        <p class="person-title">SECURITY DOORS &amp; FLYSCREENS</p>
      </div>
      <div class="contacts">
        <p class="contact">
          <svg viewBox="0 0 14 14"><circle cx="7" cy="7" r="7" fill="var(--icon)"/><path d="M4.5 3.8l1.4-.3.7 1.7-.9.7c.4.9 1 1.5 1.9 1.9l.7-.9 1.7.7-.3 1.4c-3 .1-5.3-2.2-5.2-5.2z" fill="#fff"/></svg>
          Ph: 8157 2604
        </p>
        <p class="contact">
          <svg viewBox="0 0 14 14"><circle cx="7" cy="7" r="7" fill="var(--icon)"/><rect x="4" y="5" width="6" height="4.5" fill="#fff"/><rect x="5" y="3.5" width="4" height="1.5" fill="#fff"/></svg>
          Fax: 8157 2609
        </p>
        <p class="contact">
          <svg viewBox="0 0 14 14"><circle cx="7" cy="7" r="7" fill="var(--icon)"/><rect x="5" y="3" width="4" height="8" rx=".8" fill="#fff"/><circle cx="7" cy="9.8" r=".5" fill="var(--icon)"/></svg>
          Gavin: 0419 275 916
        </p>
        <p class="contact">
          <svg viewBox="0 0 14 14"><circle cx="7" cy="7" r="7" fill="var(--icon)"/><circle cx="7" cy="7" r="3.6" fill="none" stroke="#fff" stroke-width="1"/><path d="M3.4 7h7.2M7 3.4c-1.6 2.2-1.6 5 0 7.2M7 3.4c1.6 2.2 1.6 5 0 7.2" fill="none" stroke="#fff" stroke-width=".8"/></svg>
          www.kmdistributors-example.net
        </p>
        <p class="contact">
          <svg viewBox="0 0 14 14"><circle cx="7" cy="7" r="7" fill="var(--icon)"/><path d="M3.6 4.5h6.8v5H3.6z" fill="#fff"/><path d="M3.6 4.5L7 7.3l3.4-2.8" fill="none" stroke="var(--icon)" stroke-width=".9"/></svg>
          gatesupplier@mailbox-example.net
        </p>
        <p class="contact">
          <svg viewBox="0 0 14 14"><circle cx="7" cy="7" r="7" fill="var(--icon)"/><path d="M7 3a2.6 2.6 0 0 1 2.6 2.6C9.6 7.6 7 11 7 11S4.4 7.6 4.4 5.6A2.6 2.6 0 0 1 7 3z" fill="#fff"/><circle cx="7" cy="5.6" r="1" fill="var(--icon)"/></svg>
          17 Larkvale Rd. Thomastown 3074
        </p>
      </div>
    </div>
    <div class="rule rule-upper"></div>
    <div class="rule rule-lower"></div>
  </section>
</body>
</html>
```